Dovekin BTFM Leadership Academy

Would like a flyer designed for this program. Playing off of the "Take Wing" tag line. The BTFM is acronym for "build trust, foster momentum". It is a leadership/people development program aimed at training human (aka "conscious") leadership skills. Maybe play around with B T F M stacked (can't get the superscript to work here). Website is www.dovekin.com. Would like the same color palette. Want a high energy, power vibe. Want a light background on the flyer.
The presentation is intended to inform the content included in the flyer. Would like succinct messaging with clean, clear aesthetic. Include high-level overview of the program details included in the ppt slides.

Target Market(s)

Organizations looking for leadership development programs

Font styles to use
Serif

Requirements
Must have
• include call to action with contact info - qr code to dovekin.com, email mave@dovekin.com

```html
<!DOCTYPE html>
<html lang="en">
<head>
<meta charset="utf-8">
<title>Dovekin – Take Wing flyer</title>
<link rel="stylesheet" href="https://fonts.googleapis.com/css2?family=Poppins:wght@400;500;600;700;800&display=swap">
<style>
:root{
  --brown:#4b3a13;
  --green:#467a22;
  --green-dark:#3d6b1d;
  --lime:#8cc43f;
  --yellow:#d8d21c;
  --ink:#3a3226;
  --muted:#5b5548;
  --rule:#c9c4b6;
  --panel:#f0efeb;
  --paper:#ffffff;
  --stage:#e4e4e4;
}
*{margin:0;padding:0;box-sizing:border-box}
html,body{width:806px;height:1200px;overflow:hidden;background:var(--stage)}
body{font-family:"Poppins",sans-serif;color:var(--ink);position:relative}

.slot{position:absolute;left:177px;width:452px;height:584px;box-shadow:0 6px 18px rgba(0,0,0,.18)}
.slot-front{top:8px}
.slot-back{top:608px}
.sheet{position:absolute;left:0;top:0;width:627px;height:811px;background:var(--paper);overflow:hidden;transform:scale(.72);transform-origin:0 0}

/* ---------- front ---------- */
.hero-photo{position:absolute;left:363px;top:0;width:264px;height:362px;
  background:linear-gradient(180deg,#6f7f9c 0%,#a9b4c6 28%,#ece8da 47%,#d9a55b 55%,#b9772d 72%,#8e5420 100%);
  border-bottom-left-radius:70px;border-left:3px solid var(--green)}
.brand{position:absolute;left:40px;top:120px;display:flex;align-items:center;gap:8px}
.brand-dot{width:13px;height:13px;border-radius:50%;background:var(--lime)}
.brand-name{font-size:26px;font-weight:600;color:var(--brown);letter-spacing:.5px}
.headline{position:absolute;left:40px;top:164px;font-size:46px;font-weight:800;color:var(--brown);line-height:1}
.headline-rule{position:absolute;left:40px;top:224px;width:296px;height:2px;background:var(--green)}
.subhead{position:absolute;left:40px;top:232px;font-size:23px;font-weight:700;line-height:1.1;text-transform:uppercase}
.subhead .l1{color:var(--brown);display:block}
.subhead .l2{color:var(--green);display:block}
.intro-band{position:absolute;left:0;top:291px;width:368px;height:72px;background:var(--brown);
  color:#fff;font-size:9px;line-height:1.25;padding:9px 12px 0 40px}

.col{position:absolute;top:383px}
.col-left{left:40px;width:270px}
.col-right{left:326px;width:254px}
.tag{display:inline-block;background:var(--green);color:#fff;font-weight:700;font-size:13px;
  padding:0 9px 0 6px;border-left:3px solid var(--brown);border-radius:0 10px 10px 0;line-height:20px}
.lead{font-size:8.5px;color:var(--muted);margin-top:5px;line-height:1.25}
.pill{display:inline-block;background:var(--brown);color:#fff;font-weight:700;font-size:9.5px;padding:0 7px;border-radius:8px;margin-top:6px;line-height:15px}
.bullets{list-style:none;font-size:9px;font-weight:600;margin-top:4px;display:grid;grid-template-columns:1fr 1fr;row-gap:4px}
.bullets li::before,.who li::before{content:"";display:inline-block;width:5px;height:5px;border-radius:50%;background:var(--lime);margin-right:5px;vertical-align:1px}
.chevrons{display:flex;margin-top:10px;height:20px}
.chev{font-size:8.5px;font-weight:600;color:#fff;display:flex;align-items:center;padding:0 11px 0 9px;margin-right:-5px;
  clip-path:polygon(0 0,calc(100% - 7px) 0,100% 50%,calc(100% - 7px) 100%,0 100%,7px 50%)}
.chev:first-child{clip-path:polygon(0 0,calc(100% - 7px) 0,100% 50%,calc(100% - 7px) 100%,0 100%);padding-left:6px}
.chev.c1{background:var(--green)}.chev.c2{background:var(--lime)}.chev.c3{background:var(--green-dark)}.chev.c4{background:var(--lime);color:var(--brown);font-weight:700}
.who{list-style:none;font-size:8.5px;line-height:1.25;margin-top:4px}
.who li{padding:4px 0 3px 11px;text-indent:-10px;border-bottom:1px solid var(--rule)}
.who li:last-child{border-bottom:none}

.modules{position:absolute;left:41px;top:549px;width:544px;height:182px;border:2px solid var(--rule);border-radius:12px;background:var(--panel);padding:6px}
.modules-title{text-align:center;font-weight:700;font-size:13px;color:var(--brown);margin-bottom:4px}
.modules-grid{display:grid;grid-template-columns:repeat(3,1fr);gap:4px;height:144px}
.module{border-radius:9px;color:#fff;padding:7px 8px 0;text-align:center}
.module.m1{background:var(--green)}.module.m2{background:var(--lime)}.module.m3{background:var(--green-dark)}
.module svg{width:24px;height:24px;display:block;margin:0 auto 3px}
.module h3{font-size:14px;font-weight:700;line-height:1.1}
.module .suite{font-size:8.5px;padding-bottom:4px;border-bottom:1px solid rgba(255,255,255,.6)}
.module ul{list-style:none;text-align:left;font-size:8.5px;margin-top:6px;line-height:1.6}
.module li::before{content:"";display:inline-block;width:5px;height:5px;border-radius:50%;background:#fff;margin-right:5px;vertical-align:1px}

.footer{position:absolute;left:0;top:746px;width:627px;height:65px;background:var(--brown);display:flex;align-items:center;justify-content:center}
.url{color:#fff;font-size:19px;letter-spacing:2.5px;font-weight:400}
.url b{color:var(--yellow);font-weight:700}

/* ---------- back ---------- */
.details{position:absolute;left:0;top:0;width:627px;height:226px;background:var(--brown);color:#fff;padding:48px 40px 0 41px}
.details .tag{font-size:13px}
.details h2{font-size:11.5px;font-weight:600;margin-top:2px;line-height:16px}
.plan{list-style:none;font-size:9.5px;line-height:16px}
.plan li::before{content:"";display:inline-block;width:5px;height:5px;border-radius:50%;background:var(--yellow);margin-right:4px;vertical-align:1px}
.plan .hi{color:var(--yellow)}
.plan .sub{padding-left:8px;color:#fff}
.plan .sub::before{background:var(--lime)}
.note{font-size:6.5px;margin-top:1px}

.process{position:absolute;left:41px;top:239px;width:544px;height:484px;border:2px solid var(--rule);border-radius:14px;background:var(--panel);overflow:hidden}
.process-head{height:86px;background:var(--green);text-align:center;padding-top:12px}
.process-head h2{font-size:28px;font-weight:800;color:var(--yellow);line-height:1.1;display:flex;align-items:center;justify-content:center;gap:6px}
.process-head h2::before,.process-head h2::after{content:"";width:60px;height:2px;background:var(--yellow);margin-top:12px}
.process-head p{font-size:16px;font-weight:700;color:#fff;text-transform:uppercase;margin-top:2px}

.axis{position:absolute;left:60px;top:357px;width:24px;height:340px}
.axis-label{position:absolute;left:60px;top:382px;width:24px;height:312px;writing-mode:vertical-rl;transform:rotate(180deg);
  font-size:11px;font-weight:700;color:var(--brown);text-align:center;line-height:24px;white-space:nowrap}
.arrows{position:absolute;left:0;top:0;width:627px;height:811px}

.step{position:absolute;height:36px;display:flex;font-size:13px;font-weight:600}
.step .num{width:53px;display:flex;align-items:center;justify-content:center;font-size:17px;font-weight:500;color:#fff}
.step .label{flex:1;background:#fff;display:flex;align-items:center;padding:0 18px;border:2px solid var(--green)}
.step.odd .num{background:var(--green-dark);border-radius:18px 0 0 18px}
.step.odd .label{border-left:none;border-radius:0 18px 18px 0}
.step.odd.flat .label{border-radius:0}
.step.even .num{background:var(--lime);border-radius:0 18px 18px 0;font-weight:700}
.step.even .label{border-right:none;border-radius:18px 0 0 18px;justify-content:center;border-color:var(--lime)}

.result{position:absolute;left:93px;top:673px;width:283px;height:24px;background:var(--green);color:#fff;font-size:13px;font-weight:700;
  display:flex;align-items:center;padding-left:9px;clip-path:polygon(0 0,calc(100% - 12px) 0,100% 50%,calc(100% - 12px) 100%,0 100%)}

.footer-back{justify-content:space-between;padding:0 40px}
.qr{width:46px;height:46px;background:#fff;border:4px solid #fff;outline:2px solid var(--lime)}
.email{color:#fff;font-size:11px;font-weight:500;width:110px;text-align:right}
.email b{color:var(--yellow);font-weight:600}
</style>
</head>
<body>

<div class="slot slot-front">
  <main class="sheet front">
    <div class="hero-photo" role="img" aria-label="Photograph of a golden wheat field under a wide sky with the sun low on the horizon"></div>

    <div class="brand"><span class="brand-dot"></span><span class="brand-name">Dovekin</span></div>
    <h1 class="headline">TAKE WING</h1>
    <div class="headline-rule"></div>
    <h2 class="subhead"><span class="l1">Build trust,</span><span class="l2">foster momentum</span></h2>

    <p class="intro-band">Dovekin helps leaders unleash creativity and innovation by developing skills in compassion, purpose, courage, inclusiveness, and decisiveness. We believe in the unlimited potential of individuals and organizations and that inspired, self-aware leadership is key to unlocking it.</p>

    <section class="col col-left">
      <span class="tag">THE OBJECTIVE</span>
      <p class="lead">To build trust, foster momentum within individuals, teams and the organization.</p>
      <span class="pill">UNLEASH</span>
      <ul class="bullets">
        <li>More engagement</li><li>More creativity</li>
        <li>More connection</li><li>More innovation</li>
        <li>More collaboration</li>
      </ul>
      <div class="chevrons">
        <span class="chev c1">Connection</span><span class="chev c2">collaboration</span><span class="chev c3">creativity</span><span class="chev c4">INNOVATION</span>
      </div>
    </section>

    <section class="col col-right">
      <span class="tag">WHO IS BTFM FOR</span>
      <ul class="who">
        <li>Anyone currently leading organizations, teams, people</li>
        <li>Anyone aspiring to lead organizations, teams and people</li>
        <li>Anyone aspiring to bring their whole-heart to work</li>
        <li>Anyone aspiring to build trust, foster momentum in themselves and others</li>
        <li>Anyone looking to scale their business with empowered people</li>
      </ul>
    </section>

    <section class="modules">
      <h2 class="modules-title">B T F M PROGRAM MODULES</h2>
      <div class="modules-grid">
        <article class="module m1">
          <svg viewBox="0 0 32 32" aria-hidden="true"><circle cx="16" cy="16" r="11" fill="none" stroke="#fff" stroke-width="4" stroke-dasharray="4 2.6"/><circle cx="16" cy="16" r="7" fill="#fff"/><circle cx="16" cy="13.5" r="2.5" fill="#467a22"/><path d="M11.5 20a4.5 4 0 0 1 9 0z" fill="#467a22"/></svg>
          <h3>INDIVIDUAL</h3>
          <p class="suite">(Change at the "You" Suite)</p>
          <ul><li>Developing self-awareness</li><li>Identifying values and purpose</li><li>Uncovering unconscious beliefs</li></ul>
        </article>
        <article class="module m2">
          <svg viewBox="0 0 32 32" aria-hidden="true" fill="#fff"><circle cx="16" cy="9" r="4"/><circle cx="8" cy="12" r="3"/><circle cx="24" cy="12" r="3"/><rect x="11" y="14" width="10" height="13" rx="3"/><rect x="4" y="16" width="8" height="10" rx="3"/><rect x="20" y="16" width="8" height="10" rx="3"/></svg>
          <h3>TEAMS</h3>
          <p class="suite">(Change at the "Us" Suite)</p>
          <ul><li>Conscious listening</li><li>Developing compassion</li><li>Building trusting relationships</li></ul>
        </article>
        <article class="module m3">
          <svg viewBox="0 0 32 32" aria-hidden="true" fill="#fff"><circle cx="16" cy="5" r="3"/><rect x="13" y="8" width="6" height="5" rx="1"/><rect x="15" y="13" width="2" height="4"/><rect x="6" y="16" width="20" height="2"/><circle cx="7" cy="21" r="2.5"/><circle cx="16" cy="21" r="2.5"/><circle cx="25" cy="21" r="2.5"/><rect x="4" y="24" width="6" height="5" rx="1"/><rect x="13" y="24" width="6" height="5" rx="1"/><rect x="22" y="24" width="6" height="5" rx="1"/></svg>
          <h3>ORGANIZATION</h3>
          <p class="suite">(Change the Suite)</p>
          <ul><li>Building safety</li><li>Creating a shared vision</li><li>Putting learning into action</li></ul>
        </article>
      </div>
    </section>

    <footer class="footer"><span class="url">www.<b>dovekin</b>.com</span></footer>
  </main>
</div>

<div class="slot slot-back">
  <main class="sheet back">
    <section class="details">
      <span class="tag">B T F M PROGRAM</span>
      <h2>Cohort-based program</h2>
      <ul class="plan">
        <li class="hi">Cohorts include 4 people each (cohorts are assigned by leadership)</li>
        <li class="hi">Bi-weekly cohort meetings (60 mins)</li>
        <li class="sub">Months 1 - 2: 4 meetings - Individual (inner skills)</li>
        <li class="sub">Months 3 - 4: 4 meetings - Team (interpersonal skills)</li>
        <li class="sub">Months 5 - 6: 4 meetings - BTFM (putting skills to work) - role-playing/real-world problem solving</li>
        <li class="hi">Monthly 1:1 coaching session for each member</li>
        <li class="hi">Final live or online video recording for each person</li>
      </ul>
      <p class="note">*Fully customizable</p>
    </section>

    <section class="process">
      <div class="process-head">
        <h2>THE B T F M PROCESS</h2>
        <p>Build trust, foster momentum</p>
      </div>
    </section>

    <svg class="arrows" viewBox="0 0 627 811" aria-hidden="true">
      <path d="M72 357 L84 372 L84 697 L60 697 L60 372 Z" fill="none" stroke="#4b3a13" stroke-width="2.5"/>
      <g fill="#8cc43f">
        <polygon points="150,391 182,413 176,413 176,455 130,455 124,449 124,413 118,413"/>
        <polygon points="150,487 182,509 176,509 176,551 130,551 124,545 124,509 118,509"/>
        <polygon points="150,584 182,606 176,606 176,648 130,648 124,642 124,606 118,606"/>
      </g>
      <g fill="#3d6b1d">
        <polygon points="512,440 545,462 537,462 537,498 531,504 486,504 486,462 479,462"/>
        <polygon points="512,536 545,558 537,558 537,594 531,600 486,600 486,558 479,558"/>
      </g>
    </svg>
    <div class="axis-label">INCREASE ORGANIZATIONAL EFFECTIVENESS</div>

    <div class="step odd" style="left:173px;top:369px;width:341px"><span class="num">01</span><span class="label">Building trust and momentum</span></div>
    <div class="step even" style="left:176px;top:417px;width:313px"><span class="label">Safety, trust and connection</span><span class="num">02</span></div>
    <div class="step odd flat" style="left:173px;top:466px;width:313px"><span class="num">03</span><span class="label">Authenticity and vulnerability</span></div>
    <div class="step even" style="left:176px;top:513px;width:313px"><span class="label">Individual inner work</span><span class="num">04</span></div>
    <div class="step odd flat" style="left:173px;top:562px;width:313px"><span class="num">05</span><span class="label">Courage and confidence</span></div>
    <div class="step even" style="left:176px;top:610px;width:313px"><span class="label">Individual inner work</span><span class="num">06</span></div>

    <div class="result">INCREASE POWER AND POTENTIAL</div>

    <footer class="footer footer-back">
      <div class="qr" role="img" aria-label="QR code linking to www.dovekin.com"></div>
      <span class="url">www.<b>dovekin</b>.com</span>
      <span class="email"><b>mave@dovekin.com</b></span>
    </footer>
  </main>
</div>

</body>
</html>
```